One-Page Flat Design for SEO Company [2 DAYS]

We need a one-page flat design for our SEO company. Our current website is http://www.rankloft.com/. We are looking to completely re-design the site using new flat design techniques.
Below are some examples of the type of style we're going after:
http://quormel.com/
http://tobyrand.co.uk/
https://pentaly.co/
http://milesporter.me/
As you can see- flat, clean, minimal. It is very important you follow this type of style.
For colour scheme, you may use one of the pre-made colour palettes from here:
http://www.vornacle.com/blog/inspiration/24-flat-designs-with-compelling-color-palettes
I've attached a wireframe to be followed.
Hi,

```html
<!DOCTYPE html>
<html lang="en">
<head>
<meta charset="utf-8">
<title>RankLoft — SEO services</title>
<link rel="stylesheet" href="https://fonts.googleapis.com/css2?family=Arimo:wght@400;700&family=Titillium+Web:wght@400;600;700&display=swap">
<style>
  :root {
    --sky-top: #1f6f78;
    --sky-mid: #7c8f8c;
    --sky-low: #c98a78;
    --sky-base: #9a6a63;
    --coral: #ff6b57;
    --coral-soft: #ff8a79;
    --coral-text: #ffe0d9;
    --teal: #43c5ab;
    --teal-deep: #2fae93;
    --plan-red: #ff6a55;
    --plan-orange: #ff8652;
    --plan-navy: #2e5068;
    --plan-sky: #80b9c5;
    --cyan: #1fd0ff;
    --white: #ffffff;
  }
  * { margin: 0; padding: 0; box-sizing: border-box; }
  html, body { width: 748px; height: 1200px; overflow: hidden; }
  body { position: relative; font-family: "Titillium Web", sans-serif; color: var(--white); background: var(--teal); }

  .hero { position: absolute; left: 0; top: 0; width: 748px; height: 334px; overflow: hidden; }
  .hero-backdrop { position: absolute; inset: 0;
    background:
      radial-gradient(ellipse 60% 40% at 30% 70%, rgba(240,170,150,.55), transparent 70%),
      radial-gradient(ellipse 50% 35% at 75% 55%, rgba(230,160,140,.45), transparent 70%),
      linear-gradient(180deg, var(--sky-top) 0%, var(--sky-mid) 30%, var(--sky-low) 60%, var(--sky-base) 100%); }
  .brand { position: absolute; top: 18px; left: 0; width: 748px; text-align: center; }
  .brand-name { font-family: "Titillium Web", sans-serif; font-weight: 700; font-size: 22px; line-height: 22px; color: var(--white); }
  .brand-tagline { font-family: "Arimo", sans-serif; font-size: 7px; letter-spacing: .3px; color: var(--white); margin-top: 1px; }
  .hero-title { position: absolute; top: 112px; left: 0; width: 748px; text-align: center;
    font-family: "Arimo", sans-serif; font-weight: 700; font-size: 38px; letter-spacing: -1.2px; }
  .hero-rule { position: absolute; top: 165px; left: 57px; width: 650px; height: 10px; }
  .hero-lead { position: absolute; top: 183px; left: 0; width: 748px; text-align: center;
    font-family: "Arimo", sans-serif; font-size: 18.5px; line-height: 22px; }
  .main-nav { position: absolute; top: 314px; left: 0; width: 748px; display: flex; justify-content: center; gap: 0; }
  .main-nav a { font-family: "Arimo", sans-serif; font-size: 7.5px; letter-spacing: .6px; color: var(--white); text-decoration: none; text-transform: uppercase; }
  .main-nav a.is-current { color: var(--cyan); font-weight: 700; font-size: 9px; letter-spacing: 1px; margin-top: -1px; }

  .why { position: absolute; top: 334px; left: 0; width: 748px; height: 386px; background: var(--coral); }
  .section-title { position: absolute; left: 0; width: 748px; text-align: center; font-weight: 600; font-size: 21px; letter-spacing: 1.3px; text-transform: uppercase; }
  .section-lead { position: absolute; left: 0; width: 748px; text-align: center; font-size: 10px; line-height: 14px; }
  .why .section-title { top: 33px; }
  .why .section-lead { top: 70px; color: var(--coral-text); }
  .slider-arrow { position: absolute; top: 168px; width: 20px; height: 64px; }
  .slider-arrow.prev { left: 32px; }
  .slider-arrow.next { left: 696px; }
  .feature { position: absolute; top: 144px; width: 160px; text-align: center; }
  .feature-icon { display: block; margin: 0 auto; width: 106px; height: 106px; }
  .feature-name { margin-top: 28px; font-weight: 700; font-size: 13.5px; letter-spacing: .6px; text-transform: uppercase; }
  .feature-text { margin-top: 6px; font-size: 9.5px; line-height: 14px; color: var(--coral-text); }

  .plans { position: absolute; top: 720px; left: 0; width: 748px; height: 480px; background: var(--teal); }
  .plans .section-title { top: 38px; }
  .plans .section-lead { top: 79px; }
  .plan-board { position: absolute; top: 108px; left: 90px; width: 575px; height: 380px; background: var(--teal-deep); }
  .plan { position: absolute; top: 7px; width: 140px; height: 380px; text-align: center; }
  .plan.red { left: 7px; background: var(--plan-red); }
  .plan.orange { left: 148px; background: var(--plan-orange); }
  .plan.navy { left: 288px; top: 0; height: 364px; background: var(--plan-navy); padding-top: 7px; }
  .plan.sky { left: 428px; background: var(--plan-sky); }
  .plan-name { margin-top: 44px; font-size: 13px; text-transform: uppercase; }
  .plan-price { margin-top: 2px; font-size: 10.5px; }
  .plan-features { list-style: none; margin-top: 38px; font-size: 10.5px; line-height: 22.3px; }
  .plan-cta { display: inline-block; margin-top: 25px; width: 85px; height: 24px; line-height: 22px; border: 1px solid var(--white);
    font-size: 10px; color: var(--white); text-decoration: none; text-transform: uppercase; }
  .plan.navy .plan-cta { background: var(--white); color: var(--plan-navy); }
</style>
</head>
<body>

<header class="hero">
  <div class="hero-backdrop" role="img" aria-label="Photograph of a cloudy sunset sky in teal and peach tones"></div>
  <div class="brand">
    <div class="brand-name">RankLoft</div>
    <div class="brand-tagline">LET US BOOST YOUR RANKINGS</div>
  </div>
  <h1 class="hero-title">Finally, SEO services that actually work.</h1>
  <svg class="hero-rule" viewBox="0 0 650 10" aria-hidden="true">
    <line x1="4" y1="5" x2="646" y2="5" stroke="#fff" stroke-width="1"/>
    <circle cx="4" cy="5" r="3.5" fill="#fff"/>
    <circle cx="646" cy="5" r="3.5" fill="#fff"/>
  </svg>
  <p class="hero-lead">Top-notch SEO services that are guaranteed to boost your search engine rankings.<br>100% Serpora-friendly.</p>
  <nav class="main-nav">
    <a class="is-current" href="#" style="margin-right:26px">Home</a>
    <a href="#" style="margin-right:26px">About</a>
    <a href="#" style="margin-right:26px">Work</a>
    <a href="#" style="margin-right:26px">Services</a>
    <a href="#" style="margin-right:26px">Team</a>
    <a href="#">Contact</a>
  </nav>
</header>

<section class="why">
  <h2 class="section-title">Why choose RankLoft</h2>
  <p class="section-lead">Fusce dapibus, tellus ac cursus commodo, tortor mauris condimentum.<br>Duis mollis, est non commodo luctus, nisi erat porttitor ligula, eget lacinia odio sem nec elit.</p>

  <svg class="slider-arrow prev" viewBox="0 0 20 64" aria-hidden="true"><polyline points="18,1 2,32 18,63" fill="none" stroke="#fff" stroke-width="1.2"/></svg>
  <svg class="slider-arrow next" viewBox="0 0 20 64" aria-hidden="true"><polyline points="2,1 18,32 2,63" fill="none" stroke="#fff" stroke-width="1.2"/></svg>

  <div class="feature" style="left:121px">
    <svg class="feature-icon" viewBox="0 0 106 106" aria-hidden="true">
      <circle cx="53" cy="53" r="53" fill="var(--coral-soft)"/>
      <rect x="28" y="27" width="50" height="48" rx="3" fill="#f4f1ea"/>
      <rect x="28" y="27" width="50" height="9" rx="3" fill="#dcd6cb"/>
      <circle cx="33" cy="31.5" r="2" fill="#e5604d"/><circle cx="39" cy="31.5" r="2" fill="#f0a33a"/><circle cx="45" cy="31.5" r="2" fill="#43c5ab"/>
      <rect x="32" y="42" width="15" height="27" fill="#3f5268"/>
      <rect x="51" y="43" width="22" height="2.5" fill="#c9c3b8"/><rect x="51" y="49" width="22" height="2.5" fill="#c9c3b8"/>
      <rect x="51" y="55" width="22" height="2.5" fill="#c9c3b8"/><rect x="51" y="61" width="22" height="2.5" fill="#c9c3b8"/>
      <rect x="51" y="67" width="14" height="2.5" fill="#c9c3b8"/>
    </svg>
    <h3 class="feature-name">Branding</h3>
    <p class="feature-text">Lorem ipsum dolor sit amet,<br>consectetuer adipiscing elit,<br>sed diam nonummy nibh.</p>
  </div>

  <div class="feature" style="left:294px">
    <svg class="feature-icon" viewBox="0 0 106 106" aria-hidden="true">
      <circle cx="53" cy="53" r="53" fill="var(--coral-soft)"/>
      <rect x="38" y="27" width="30" height="7" fill="#e0574a"/>
      <rect x="38" y="34" width="30" height="25" fill="#f2c14e"/>
      <rect x="48" y="34" width="10" height="25" fill="#e8ad38"/>
      <polygon points="38,59 68,59 53,80" fill="#f1d3a6"/>
      <polygon points="48.5,73.5 57.5,73.5 53,80" fill="#3f5268"/>
    </svg>
    <h3 class="feature-name">Design</h3>
    <p class="feature-text">Sed ut perspiciatis unde<br>omnis iste natus error sit<br>voluptatem</p>
  </div>

  <div class="feature" style="left:468px">
    <svg class="feature-icon" viewBox="0 0 106 106" aria-hidden="true">
      <circle cx="53" cy="53" r="53" fill="var(--coral-soft)"/>
      <polyline points="38,40 24,53 38,66" fill="none" stroke="#fff" stroke-width="5" stroke-linecap="round" stroke-linejoin="round"/>
      <polyline points="68,40 82,53 68,66" fill="none" stroke="#fff" stroke-width="5" stroke-linecap="round" stroke-linejoin="round"/>
      <line x1="58" y1="34" x2="48" y2="72" stroke="#fff" stroke-width="5" stroke-linecap="round"/>
    </svg>
    <h3 class="feature-name">Development</h3>
    <p class="feature-text">At vero eos et accusamus et<br>iusto odio dignissimos qui<br>blanditiis praesentium.</p>
  </div>
</section>

<section class="plans">
  <h2 class="section-title">Select a Booster Plan</h2>
  <p class="section-lead">Neque porro quisquam est, qui dolorem ipsum quia dolor sit amet</p>
  <div class="plan-board">
    <article class="plan red">
      <h3 class="plan-name">Enterprise</h3>
      <p class="plan-price">$40/Month</p>
      <ul class="plan-features"><li>Free feature one</li><li>Unlimited feature two</li><li>Unlimited feature three</li><li>2x feature four</li><li>100x feature five</li></ul>
      <a class="plan-cta" href="#">Get started</a>
    </article>
    <article class="plan orange">
      <h3 class="plan-name">Enterprise</h3>
      <p class="plan-price">$40/Month</p>
      <ul class="plan-features"><li>Free feature one</li><li>Unlimited feature two</li><li>Unlimited feature three</li><li>2x feature four</li><li>100x feature five</li></ul>
      <a class="plan-cta" href="#">Get started</a>
    </article>
    <article class="plan navy">
      <h3 class="plan-name">Enterprise</h3>
      <p class="plan-price">$40/Month</p>
      <ul class="plan-features"><li>Free feature one</li><li>Unlimited feature two</li><li>Unlimited feature three</li><li>2x feature four</li><li>100x feature five</li></ul>
      <a class="plan-cta" href="#">Get started</a>
    </article>
    <article class="plan sky">
      <h3 class="plan-name">Enterprise</h3>
      <p class="plan-price">$40/Month</p>
      <ul class="plan-features"><li>Free feature one</li><li>Unlimited feature two</li><li>Unlimited feature three</li><li>2x feature four</li><li>100x feature five</li></ul>
      <a class="plan-cta" href="#">Get started</a>
    </article>
  </div>
</section>

</body>
</html>
```